Create a basic website for a new air cargo consultancy, called 'Veltrane Loadwise'

We want to build a basic website (homepage, 'about us' page, services and contact us page).
We have a logo, we have most of the text to be inserted, but not all. We also still need to take pictures.
We would like to have a fresh and modern, but business like design and the creation of the website.
We want to be able to modify the website after (add pictures and more text, update references).
We already have a url.

```html
<!DOCTYPE html>
<html lang="en">
<head>
<meta charset="utf-8">
<title>Veltrane Loadwise – Air Cargo Consultancy</title>
<link href="https://fonts.googleapis.com/css2?family=Cinzel:wght@400;500;600&family=Lato:ital,wght@0,400;0,700;1,400&display=swap" rel="stylesheet">
<style>
:root{
  --blue:#2a3592;
  --blue-dark:#232c80;
  --gold:#d4a02a;
  --gold-soft:#ecd9a6;
  --ink:#2b2b2b;
  --muted:#555;
  --band:#e9e9f3;
  --field:#f4f4f4;
  --white:#fff;
}
*{box-sizing:border-box;margin:0;padding:0}
html,body{width:1200px;height:3247px;overflow:hidden;background:var(--white)}
body{position:relative;font-family:'Lato',sans-serif;color:var(--ink)}
.abs{position:absolute}
.serif{font-family:'Cinzel',serif}
.btn{position:absolute;background:var(--gold);color:var(--white);border-radius:26px;font:700 15px 'Lato',sans-serif;display:flex;align-items:center;justify-content:center;width:156px;height:50px;letter-spacing:.2px}

/* header */
.topline{left:0;top:0;width:1200px;height:4px;background:var(--gold)}
.header{left:0;top:4px;width:1200px;height:92px;background:var(--white)}
.brand{left:111px;top:18px;width:190px}
.brand-name{font:600 34px 'Cinzel',serif;color:var(--gold);line-height:1}
.brand-tag{font:700 9px 'Lato',sans-serif;letter-spacing:3px;color:var(--gold);margin-top:6px}
.contact-item{display:flex;align-items:center;gap:18px;font-size:15px;color:#333}
.ring{width:40px;height:40px;border:1.5px solid var(--gold);border-radius:50%;display:flex;align-items:center;justify-content:center}
.social{width:32px;height:32px;border-radius:50%;background:var(--gold)}
.nav{left:447px;top:59px;width:753px;height:44px;background:var(--blue)}
.nav-wedge{left:432px;top:59px}
.nav ul{list-style:none;display:flex;position:absolute;left:91px;top:13px;gap:0}
.nav li{color:var(--white);font-size:15px;font-weight:700;margin-right:54px}

/* hero */
.hero{left:0;top:96px;width:1200px;height:740px}
.hero-photo{position:absolute;inset:0;background:
  linear-gradient(90deg,rgba(42,53,146,.95) 0%,rgba(42,53,146,.75) 35%,rgba(42,53,146,0) 60%),
  linear-gradient(170deg,#5a6aa8 0%,#b98a90 35%,#e79a5a 55%,#6a6d90 75%,#3b4478 100%)}
.hero-copy{left:111px;top:120px;width:490px;color:var(--white)}
.hero-kicker{font:500 35px 'Cinzel',serif;letter-spacing:1px}
.hero-title{font:500 84px 'Cinzel',serif;line-height:100px;margin-top:12px}
.hero-text{font-size:15.5px;line-height:26px;margin-top:16px;text-align:justify}

/* section titles */
.title{left:0;width:1200px;text-align:center;font:500 40px 'Cinzel',serif;color:var(--ink)}
.mark{background:linear-gradient(transparent 66%,var(--gold-soft) 66%)}

/* about */
.about-photo{left:140px;top:1001px;width:921px;height:193px;border-radius:8px;background:linear-gradient(180deg,#7d4c33 0%,#d08a52 40%,#a06238 70%,#3b2a22 100%)}
.about-text{left:160px;top:1242px;width:880px;text-align:center;font-size:15.5px;line-height:29px;color:#333}
.feature{width:240px;text-align:center}
.feature-pic{width:146px;height:146px;border-radius:50%;border:2px solid var(--gold);margin:0 auto}
.feature h3{font:400 19px 'Lato',sans-serif;margin-top:20px;color:#222}
.feature p{font-size:13.5px;line-height:20px;color:var(--muted);margin-top:10px}
.dot{width:19px;height:19px;border-radius:50%;background:var(--gold);margin:18px auto 0;display:flex;align-items:center;justify-content:center}

/* services */
.services{left:0;top:1843px;width:1200px;height:514px;background:var(--band)}
.card{top:2041px;width:305px;height:216px;background:var(--white);box-shadow:0 1px 6px rgba(0,0,0,.08);padding:22px 18px}
.card h3{font:500 21px 'Cinzel',serif;margin-top:16px;color:#222}
.card p{font-size:11.5px;line-height:16.5px;color:var(--muted);margin-top:12px;width:265px}
.card .go{position:absolute;right:18px;bottom:14px}

/* contact */
.field{background:var(--field);font:italic 13px 'Lato',sans-serif;color:#888;padding:18px 20px}

/* footer */
.footer{left:0;top:2929px;width:1200px;height:318px;background:var(--blue);color:var(--white)}
.foot-brand{left:111px;top:70px}
.foot-brand .brand-name{color:var(--white);font-size:44px}
.foot-brand .brand-tag{color:var(--white);font-size:10px}
.col{top:66px;font-size:15px}
.col h4{font:400 17px 'Lato',sans-serif;margin-bottom:10px}
.col li{list-style:none;line-height:28.4px}
.col .lbl{color:var(--gold)}
.copy{left:0;top:272px;width:1200px;text-align:center;font-size:15px}
</style>
</head>
<body>

<div class="abs topline"></div>
<header class="abs header"></header>
<div class="abs brand">
  <div class="brand-name">Veltrane</div>
  <div class="brand-tag">AIR CARGO · MARA LINDEN</div>
</div>
<div class="abs contact-item" style="left:479px;top:10px;height:40px">
  <div class="ring"><svg width="16" height="16" viewBox="0 0 24 24"><path d="M6.6 10.8a15 15 0 0 0 6.6 6.6l2.2-2.2c.3-.3.7-.4 1-.2 1.1.4 2.3.6 3.6.6.6 0 1 .4 1 1V20c0 .6-.4 1-1 1A17 17 0 0 1 3 4c0-.6.4-1 1-1h3.5c.6 0 1 .4 1 1 0 1.3.2 2.5.6 3.6.1.3 0 .7-.2 1z" fill="var(--gold)"/></svg></div>
  <span>+1 888 888 8888</span>
</div>
<div class="abs contact-item" style="left:710px;top:10px;height:40px">
  <div class="ring"><svg width="16" height="12" viewBox="0 0 16 12"><rect width="16" height="12" rx="1.5" fill="var(--gold)"/><path d="M1 1l7 5 7-5" stroke="#fff" stroke-width="1.4" fill="none"/></svg></div>
  <span>info@veltraneloadwise.com</span>
</div>
<div class="abs social" style="left:1018px;top:14px"></div>
<div class="abs social" style="left:1056px;top:14px"></div>

<svg class="abs nav-wedge" width="30" height="44" viewBox="0 0 30 44"><path d="M22 0h8L8 44H0z" fill="var(--gold)"/></svg>
<nav class="abs nav">
  <ul><li>HOME</li><li>ABOUT US</li><li>SERVICES</li><li>CONTACT US</li></ul>
</nav>

<section class="abs hero">
  <div class="hero-photo" role="img" aria-label="Cargo aircraft on a wet runway at sunset beside stacked freight crates"></div>
  <svg class="abs" style="left:0;top:600px" width="1200" height="140" viewBox="0 0 1200 140">
    <path d="M0 130 L0 130 L0 140 L1200 140 L1200 0 Q 1000 95 600 110 Q 300 120 0 130Z" fill="var(--white)"/>
    <path d="M0 134 L0 140 L1200 140 L1200 40 Q 1000 110 560 118 Q 300 125 0 134Z" fill="var(--white)"/>
    <path d="M340 104 Q 800 100 1200 20 L1200 32 Q 800 118 340 106Z" fill="var(--gold)"/>
    <path d="M0 132 L0 140 L1200 140 L1200 32 Q 800 118 340 110 Q 160 112 0 132Z" fill="var(--white)"/>
  </svg>
  <svg class="abs" style="left:0;top:580px" width="1200" height="160" viewBox="0 0 1200 160">
    <path d="M0 154 L0 160 L1200 160 L1200 0 L1200 15 Q 980 98 620 128 Q 420 144 300 160 Z" fill="none"/>
    <path d="M0 152 L0 160 L1200 160 L1200 112 Q 1000 140 540 150 Z" fill="none"/>
  </svg>
</section>
<svg class="abs" style="left:0;top:680px" width="1200" height="140" viewBox="0 0 1200 140">
  <path d="M0 52 Q 300 110 560 117 Q 900 115 1200 40 L1200 20 Q 1000 70 700 80 Q 300 80 0 50Z" fill="var(--blue)"/>
  <path d="M0 52 Q 300 110 560 117 Q 900 115 1200 40 L1200 140 L0 140Z" fill="var(--white)"/>
  <path d="M340 124 Q 800 126 1200 42 L1200 56 Q 820 136 340 126Z" fill="var(--gold)"/>
  <path d="M280 114 Q 620 122 1200 20 L1200 40 Q 900 115 560 117 Q 420 118 280 114Z" fill="var(--blue)"/>
</svg>
<div class="abs hero-copy">
  <div class="hero-kicker">WELCOME TO</div>
  <h1 class="hero-title">VELTRANE LOADWISE</h1>
  <p class="hero-text">Your premier consultancy specialized in the air cargo sector. We are dedicated to helping clients enhance their overall cargo strategy, drive digital transformation, foster community building, and achieve sustainability goals.</p>
</div>
<div class="btn" style="left:111px;top:610px">LEARN MORE</div>

<!-- about -->
<h2 class="abs title" style="top:902px">ABOUT VELTRANE <span class="mark">LOADWISE</span></h2>
<div class="abs about-photo" role="img" aria-label="Cargo aircraft at dusk on the apron with loaded freight pallets"></div>
<p class="abs about-text">At Veltrane Loadwise, we understand the unique challenges and opportunities within the air cargo industry. Our team of seasoned professionals offers in-depth expertise and tailored solutions to optimize your logistics operations, streamline processes, and improve efficiency. With a focus on strategic planning, we help you navigate the complexities of the global cargo landscape, ensuring your business stays competitive and resilient.</p>
<div class="btn" style="left:522px;top:1384px">LEARN MORE</div>

<div class="abs feature" style="left:109px;top:1482px">
  <div class="feature-pic" role="img" aria-label="Team planning around charts on a table" style="background:linear-gradient(160deg,#8a7a6e,#d9d2c8 60%,#6b84b8)"></div>
  <h3>Strategic Planning</h3>
  <p>strategic planning, we help you navi-<br>gate the complexities of</p>
  <div class="dot"><svg width="7" height="9" viewBox="0 0 7 9"><path d="M1.5 1l4 3.5-4 3.5" stroke="#fff" stroke-width="1.6" fill="none"/></svg></div>
</div>
<div class="abs feature" style="left:359px;top:1482px">
  <div class="feature-pic" role="img" aria-label="Digital network visual with glowing screens" style="background:linear-gradient(160deg,#0d2c4a,#1d8fb8 55%,#0b1d33)"></div>
  <h3>Digitalization</h3>
  <p>Digitalization is at the core of our<br>approach.</p>
  <div class="dot"><svg width="7" height="9" viewBox="0 0 7 9"><path d="M1.5 1l4 3.5-4 3.5" stroke="#fff" stroke-width="1.6" fill="none"/></svg></div>
</div>
<div class="abs feature" style="left:607px;top:1482px">
  <div class="feature-pic" role="img" aria-label="Joined hands against a blue sky" style="background:linear-gradient(180deg,#9cc3e8,#dbe8f4 60%,#b58c6e)"></div>
  <h3>Community building</h3>
  <p>Community building is another key<br>aspect of our consultancy.</p>
  <div class="dot"><svg width="7" height="9" viewBox="0 0 7 9"><path d="M1.5 1l4 3.5-4 3.5" stroke="#fff" stroke-width="1.6" fill="none"/></svg></div>
</div>
<div class="abs feature" style="left:857px;top:1482px">
  <div class="feature-pic" role="img" aria-label="Small globe resting in fresh green grass" style="background:linear-gradient(180deg,#cfe6a8,#7cb348 60%,#3e7a2a)"></div>
  <h3>Sustainability</h3>
  <p>Sustainability is integral to our mis-<br>sion. We work with clients to</p>
  <div class="dot"><svg width="7" height="9" viewBox="0 0 7 9"><path d="M1.5 1l4 3.5-4 3.5" stroke="#fff" stroke-width="1.6" fill="none"/></svg></div>
</div>

<!-- services -->
<section class="abs services"></section>
<h2 class="abs title" style="top:1933px">OUR <span class="mark">SERVICES</span></h2>

<div class="abs card" style="left:111px">
  <svg width="52" height="50" viewBox="0 0 52 50" fill="none" stroke="#222" stroke-width="1.8"><path d="M4 18l14 4 14-14c3-3 7-2 5 2L24 24l4 14-4 3-7-11-8 7 1 6-3 2-3-8-8-3 2-3 6 1 7-8z"/><rect x="34" y="28" width="14" height="10"/><rect x="26" y="38" width="10" height="10"/><rect x="38" y="38" width="10" height="10"/></svg>
  <h3>LOREM IPSUM</h3>
  <p>Lorem ipsum dolor sit amet, consectetur adipiscing elit, sed do eiusmod tempor incididunt ut labore et dolore magna aliqua. Ut enim ad minim veniam, quis nostrud exercitation</p>
  <svg class="go" width="22" height="10" viewBox="0 0 22 10"><path d="M0 5h20M15 1l5 4-5 4" stroke="var(--blue)" stroke-width="1.6" fill="none"/></svg>
</div>
<div class="abs card" style="left:447px">
  <svg width="52" height="50" viewBox="0 0 52 50" fill="none" stroke="var(--gold)" stroke-width="1.8"><path d="M6 16l14 4 14-14c3-3 7-2 5 2L26 22l4 14-4 3-7-11-8 7 1 6-3 2-3-8-8-3 2-3 6 1 7-8z"/><path d="M14 44l4-4M20 46l3-3M40 30l4 4"/></svg>
  <h3>LOREM IPSUM DOLOR</h3>
  <p>Lorem ipsum dolor sit amet, consectetur adipiscing elit, sed do eiusmod tempor incididunt ut labore et dolore magna aliqua. Ut enim ad minim veniam, quis nostrud exercitation</p>
  <svg class="go" width="22" height="10" viewBox="0 0 22 10"><path d="M0 5h20M15 1l5 4-5 4" stroke="var(--gold)" stroke-width="1.6" fill="none"/></svg>
</div>
<div class="abs card" style="left:783px">
  <svg width="52" height="50" viewBox="0 0 52 50" fill="none" stroke="#222" stroke-width="1.8"><circle cx="12" cy="38" r="8"/><path d="M4 38h16M12 30v16"/><rect x="40" y="4" width="10" height="10"/><rect x="22" y="20" width="12" height="12" rx="2"/><path d="M20 8a18 18 0 0 1 18 0M36 40a18 18 0 0 0 10-16"/></svg>
  <h3>LOREM IPSUM</h3>
  <p>Lorem ipsum dolor sit amet, consectetur adipiscing elit, sed do eiusmod tempor incididunt ut labore et dolore magna aliqua. Ut enim ad minim veniam, quis nostrud exercitation</p>
  <svg class="go" width="22" height="10" viewBox="0 0 22 10"><path d="M0 5h20M15 1l5 4-5 4" stroke="var(--blue)" stroke-width="1.6" fill="none"/></svg>
</div>

<!-- contact -->
<h2 class="abs title" style="top:2441px"><span class="mark">CONTACT</span> US</h2>
<div class="abs field" style="left:247px;top:2528px;width:347px;height:51px">First Name</div>
<div class="abs field" style="left:606px;top:2528px;width:347px;height:51px">Last Name</div>
<div class="abs field" style="left:247px;top:2587px;width:347px;height:51px">Phone</div>
<div class="abs field" style="left:606px;top:2587px;width:347px;height:51px">Email</div>
<div class="abs field" style="left:247px;top:2647px;width:706px;height:113px">Message</div>
<div class="btn" style="left:522px;top:2784px">SUBMIT</div>

<!-- footer -->
<footer class="abs footer">
  <div class="abs foot-brand">
    <div class="brand-name">Veltrane</div>
    <div class="brand-tag">AIR CARGO · MARA LINDEN</div>
  </div>
  <div class="abs social" style="left:111px;top:200px;background:var(--white)"></div>
  <div class="abs social" style="left:150px;top:200px;background:var(--white)"></div>
  <div class="abs col" style="left:514px">
    <h4>QUICK LINKS</h4>
    <ul><li>Home</li><li>About us</li><li>Services</li><li>Contact us</li></ul>
  </div>
  <div class="abs col" style="left:712px">
    <h4>ABOT US</h4>
    <ul><li>Sitemap</li><li>Disclaimer</li><li>Privacy Statement</li><li>Contact Us</li></ul>
  </div>
  <div class="abs col" style="left:904px">
    <h4>OTHER LINKS</h4>
    <ul><li class="lbl">Address</li><li>Lorem ipsum dolor sit</li><li class="lbl">Phone</li><li>+1 (888) 888 8888</li><li class="lbl">Email</li><li>info@veltraneloadwise.com</li></ul>
  </div>
  <div class="abs copy">© 2024 Veltrane Loadwise. All Rights Reserved.</div>
</footer>

</body>
</html>
```